- New restaurant page
- I will like to use this page to advertise and mention the grand opening
- QR brand and logo is well known
- Brightwater Fish & Chicken on Larkmoor Crest
- I attached professional pictures that were taking recently
- Initially i will like the design and the facebook logo and the cover photo. in the cover photo I will include the address, phone number and that you can order on Platewagon, mealnest and Plate wagon
- then I will like professional edit the pictures and include the store info.
- this a link of a similar design that i will like to try out. https://www.facebook.com/qrfishvaldane
- address 3167 S Larkmoor Cr Ave,
Chicago, IL 60592
- phone number 7735104286
- email: info@qrfishandchickenonlarkmoor.example

Target Market(s)

facebook for now.

Industry/Entity Type

resturant

Colors
EB3D1F
EC4F4E
F09395
F8D3D4
FCEDEE

Requirements
Must have
• facebook cover photo with contact info and nice design. pictures to post for the grand opening in nice designs
Nice to have
• look at this for ideas https://www.facebook.com/qrfishvaldane

```html
<!DOCTYPE html>
<html lang="en">
<head>
<meta charset="utf-8">
<title>Brightwater Fish &amp; Chicken – Grand Opening Cover</title>
<link href="https://fonts.googleapis.com/css2?family=Great+Vibes&family=Montserrat:wght@400;500;600;700&display=swap" rel="stylesheet">
<style>
  :root {
    --red-deep: #EB3D1F;
    --red: #EC4F4E;
    --rose: #F09395;
    --blush: #F8D3D4;
    --cream: #FCEDEE;
    --paper: #F4E7E7;
    --ink: #1E1A1A;
    --white: #FFFFFF;
    --stage: #F3F3F3;
  }
  * { box-sizing: border-box; margin: 0; padding: 0; }
  html, body { width: 1200px; height: 1200px; overflow: hidden; }
  body { background: var(--stage); font-family: "Montserrat", sans-serif; position: relative; }

  .cover-frame {
    position: absolute; left: 50px; top: 396px;
    width: 1100px; height: 407px; overflow: hidden;
  }
  .cover {
    position: absolute; left: 0; top: 0;
    width: 864px; height: 320px;
    transform: scale(1.27315); transform-origin: 0 0;
    background: var(--paper);
    overflow: hidden;
  }
  .cover__waves { position: absolute; inset: 0; width: 864px; height: 320px; }

  .headline { position: absolute; left: 40px; top: 38px; }
  .headline__script {
    position: absolute; left: 0; top: 0;
    font-family: "Great Vibes", cursive; font-size: 38px; color: var(--ink);
    line-height: 1; z-index: 2;
  }
  .headline__main {
    position: absolute; left: 0; top: 28px; white-space: nowrap;
    font-size: 42px; font-weight: 500; letter-spacing: 0.5px; line-height: 1;
    color: transparent; -webkit-text-stroke: 1.2px var(--red-deep);
  }

  .store-info { position: absolute; left: 140px; top: 154px; color: var(--white); }
  .store-info__address { font-size: 8.5px; font-weight: 500; line-height: 1.35; }
  .store-info__row { display: flex; align-items: center; gap: 7px; margin-top: 12px; }
  .store-info__phone { font-size: 13px; font-weight: 500; letter-spacing: 0.3px; }
  .store-info__email { font-size: 9px; font-weight: 400; }
  .store-info__row--email { margin-top: 8px; }
  .icon { width: 12px; height: 12px; flex: none; }

  .order-bar {
    position: absolute; left: 140px; top: 259px;
    width: 233px; height: 25px; border-radius: 13px;
    background: var(--white); display: flex; align-items: center;
    box-shadow: 0 2px 5px rgba(150, 40, 30, 0.18);
  }
  .order-bar__cta {
    width: 104px; height: 25px; border-radius: 13px;
    background: var(--red-deep); color: var(--white);
    font-size: 8px; font-weight: 700; letter-spacing: 0.4px;
    display: flex; align-items: center; justify-content: center;
  }
  .order-bar__partner { font-size: 11px; font-weight: 600; color: var(--ink); margin-left: 14px; }
  .order-bar__partner--small {
    font-size: 7px; color: var(--red-deep); margin-left: 12px;
    display: flex; align-items: center; gap: 3px;
  }
  .partner-dot { width: 7px; height: 7px; border-radius: 50%; background: var(--red-deep); }

  .brand-tile {
    position: absolute; left: 40px; top: 258px;
    width: 61px; height: 70px; border-radius: 8px;
    background: var(--white);
    display: flex; align-items: flex-start; justify-content: center;
    padding-top: 14px;
    box-shadow: 0 2px 6px rgba(120, 30, 30, 0.2);
  }
  .brand-tile__name {
    font-size: 7.5px; font-weight: 700; color: var(--red-deep);
    text-align: center; line-height: 1.15;
  }

  .photo {
    position: absolute; border-radius: 9px; overflow: hidden;
    border: 1px solid rgba(255, 255, 255, 0.6);
  }
  .photo--fish { left: 509px; top: -8px; width: 156px; height: 84px;
    background: radial-gradient(circle at 55% 50%, #D9A056, #EEDCC2 70%, #F5F1EC); }
  .photo--burger { left: 509px; top: 82px; width: 156px; height: 122px;
    background: radial-gradient(ellipse at 50% 50%, #B6762E, #7A4A22 45%, #A9B7C2 90%); }
  .photo--wings { left: 509px; top: 210px; width: 156px; height: 118px;
    background: radial-gradient(ellipse at 50% 50%, #8E2A14, #B8461F 50%, #E0C3A8 95%); }
  .photo--steak-fries { left: 671px; top: -8px; width: 157px; height: 117px;
    background: radial-gradient(ellipse at 60% 55%, #E7B24A, #C48A48 50%, #EDE5DC 95%); }
  .photo--shrimp { left: 671px; top: 115px; width: 157px; height: 120px;
    background: radial-gradient(ellipse at 55% 50%, #F2B53A, #F0D27E 45%, #F4F1EA 90%); }
  .photo--sandwich { left: 671px; top: 241px; width: 157px; height: 87px;
    background: radial-gradient(ellipse at 50% 40%, #B8742F, #D7A15E 45%, #ECE6DF 90%); }
</style>
</head>
<body>
  <div class="cover-frame">
    <section class="cover" aria-label="Grand opening cover for Brightwater Fish &amp; Chicken">
      <svg class="cover__waves" viewBox="0 0 864 320" aria-hidden="true">
        <defs>
          <linearGradient id="waveMain" x1="0" y1="0" x2="1" y2="1">
            <stop offset="0" stop-color="#F09395"/>
            <stop offset="0.55" stop-color="#EC4F4E"/>
            <stop offset="1" stop-color="#EB3D1F"/>
          </linearGradient>
          <linearGradient id="waveSoft" x1="0" y1="0" x2="1" y2="0">
            <stop offset="0" stop-color="#F8D3D4" stop-opacity="0.55"/>
            <stop offset="1" stop-color="#F09395" stop-opacity="0.3"/>
          </linearGradient>
          <linearGradient id="sideBand" x1="0" y1="0" x2="0" y2="1">
            <stop offset="0" stop-color="#EC4F4E"/>
            <stop offset="1" stop-color="#EB3D1F"/>
          </linearGradient>
        </defs>
        <path d="M0,138 C110,118 230,140 330,185 C420,225 470,240 505,205 L505,0 L864,0 L864,320 L0,320 Z" fill="url(#waveMain)"/>
        <path d="M0,170 C120,150 240,175 340,220 C430,260 480,270 520,240 L520,320 L0,320 Z" fill="url(#waveSoft)"/>
        <path d="M0,215 C140,195 260,225 360,260 C430,285 480,300 520,290 L520,320 L0,320 Z" fill="#EC4F4E" fill-opacity="0.35"/>
        <path d="M490,0 C520,60 500,140 540,200 C570,250 540,290 560,320 L864,320 L864,0 Z" fill="url(#sideBand)" fill-opacity="0.7"/>
      </svg>

      <div class="headline">
        <span class="headline__script">The</span>
        <h1 class="headline__main">GRAND OPENING</h1>
      </div>

      <div class="store-info">
        <p class="store-info__address">3167 S Larkmoor Cr Ave,<br>Chicago, IL 60592</p>
        <p class="store-info__row">
          <svg class="icon" viewBox="0 0 24 24" aria-hidden="true"><path fill="#FFFFFF" d="M6.6 10.8a15.1 15.1 0 0 0 6.6 6.6l2.2-2.2c.3-.3.7-.4 1-.2 1.1.4 2.3.6 3.6.6.6 0 1 .4 1 1V20c0 .6-.4 1-1 1A17 17 0 0 1 3 4c0-.6.4-1 1-1h3.5c.6 0 1 .4 1 1 0 1.3.2 2.5.6 3.6.1.3 0 .7-.2 1l-2.3 2.2z"/></svg>
          <span class="store-info__phone">7735104286</span>
        </p>
        <p class="store-info__row store-info__row--email">
          <svg class="icon" viewBox="0 0 24 24" aria-hidden="true"><rect x="2" y="5" width="20" height="14" rx="2" fill="none" stroke="#FFFFFF" stroke-width="2"/><path d="M3 6l9 7 9-7" fill="none" stroke="#FFFFFF" stroke-width="2"/></svg>
          <span class="store-info__email">info@qrfishandchickenonlarkmoor.example</span>
        </p>
      </div>

      <div class="order-bar">
        <span class="order-bar__cta">ORDER NOW</span>
        <span class="order-bar__partner">Platewagon</span>
        <span class="order-bar__partner order-bar__partner--small"><span class="partner-dot"></span>mealnest</span>
      </div>

      <div class="brand-tile">
        <span class="brand-tile__name">Brightwater<br>Fish &amp; Chicken</span>
      </div>

      <div class="photo photo--fish" role="img" aria-label="Fried fish fillets with dipping sauce on a tray"></div>
      <div class="photo photo--burger" role="img" aria-label="Cheeseburger with lettuce and tomato beside fries"></div>
      <div class="photo photo--wings" role="img" aria-label="Glazed chicken wings with fries"></div>
      <div class="photo photo--steak-fries" role="img" aria-label="Steak sandwich with a heap of fries"></div>
      <div class="photo photo--shrimp" role="img" aria-label="Fried jumbo shrimp with dipping sauce"></div>
      <div class="photo photo--sandwich" role="img" aria-label="Loaded sandwich with lettuce and tomato"></div>
    </section>
  </div>
</body>
</html>
```